Boutique Wealth management firm needs a new business card design

I want to update my business card design to be more consistent with the look and feel of my website (www.brisvane-wealth.com). I would like to incorporate an ivory parchment background and am open to switching from the current "portrait" layout to a more traditional "landscape" orientation. The final design should convey stability and exclusivity and I want something in PDF format that is ready to send to the printer

Thank you all for taking the time to submit your designs for my project. I've made my decision and picked the design I like best. Thanks again!

```html
<!DOCTYPE html>
<html lang="en">
<head>
<meta charset="utf-8">
<title>Brisvane Wealth Advisory — Business Card</title>
<link rel="stylesheet" href="https://fonts.googleapis.com/css2?family=Lato:wght@400;700;900&display=swap">
<style>
  :root {
    --backdrop: #2b2b2d;
    --parchment-light: #f2e2ad;
    --parchment-mid: #e8d397;
    --parchment-edge: #d9bf7f;
    --plum: #6b2542;
    --ink: #1c1a18;
  }
  * { box-sizing: border-box; margin: 0; padding: 0; }
  html, body {
    width: 1200px; height: 1000px; overflow: hidden;
    background: var(--backdrop);
    font-family: "Lato", Arial, sans-serif;
  }
  .business-card {
    position: absolute;
    left: 110px; top: 220px;
    width: 980px; height: 560px;
    background:
      radial-gradient(ellipse at 35% 40%, var(--parchment-light) 0%, var(--parchment-mid) 60%, var(--parchment-edge) 100%);
    box-shadow: 0 20px 50px rgba(0,0,0,0.5);
  }
  .brand-name {
    position: absolute;
    left: 70px; top: 240px;
    font-weight: 900;
    font-size: 44px;
    line-height: 1.1;
    color: var(--plum);
    letter-spacing: 0.5px;
  }
  .contact-column {
    position: absolute;
    left: 560px; top: 70px;
    color: var(--ink);
  }
  .person-name {
    font-weight: 900;
    font-size: 38px;
    color: var(--plum);
  }
  .person-name sup { font-size: 20px; }
  .person-title {
    font-weight: 700;
    font-size: 22px;
    margin: 4px 0 0 18px;
  }
  .contact-list {
    list-style: none;
    margin: 34px 0 0 48px;
  }
  .contact-list li {
    display: flex; align-items: center;
    font-size: 23px;
    line-height: 34px;
  }
  .contact-list svg {
    width: 22px; height: 22px;
    margin-right: 14px;
    fill: var(--plum);
  }
  .mailing-address {
    margin: 42px 0 0 72px;
    font-size: 23px;
    line-height: 30px;
  }
  .mailing-address strong { font-weight: 900; display: block; }
  .license-note {
    position: absolute;
    right: 70px; bottom: 48px;
    font-size: 23px;
    color: var(--ink);
  }
</style>
</head>
<body>
  <article class="business-card">
    <div class="brand-name">Brisvane Wealth Advisory</div>

    <div class="contact-column">
      <div class="person-name">Dale Morrow, CFP<sup>®</sup></div>
      <div class="person-title">Principal</div>

      <ul class="contact-list">
        <li>
          <svg viewBox="0 0 24 24" aria-hidden="true"><path d="M6.6 10.8c1.4 2.8 3.8 5.1 6.6 6.6l2.2-2.2c.3-.3.7-.4 1-.2 1.1.4 2.3.6 3.6.6.6 0 1 .4 1 1V20c0 .6-.4 1-1 1C10.6 21 3 13.4 3 4c0-.6.4-1 1-1h3.5c.6 0 1 .4 1 1 0 1.3.2 2.5.6 3.6.1.3 0 .7-.2 1z"/></svg>
          555-014-2876
        </li>
        <li>
          <svg viewBox="0 0 24 24" aria-hidden="true"><path d="M2 5h20v14H2z M2 5l10 8 10-8" fill="var(--plum)"/><path d="M3 6l9 7 9-7" stroke="var(--parchment-light)" stroke-width="1.6" fill="none"/></svg>
          dale@brisvane-wealth.com
        </li>
        <li>
          <svg viewBox="0 0 24 24" aria-hidden="true"><circle cx="12" cy="12" r="10"/><path d="M2 12h20M12 2c3 3 3 17 0 20M12 2c-3 3-3 17 0 20" stroke="var(--parchment-light)" stroke-width="1.4" fill="none"/></svg>
          www.brisvane-wealth.com
        </li>
      </ul>

      <address class="mailing-address" style="font-style:normal">
        <strong>Mailing Address:</strong>
        2280 Alder Ridge Rd. #114,<br>
        Fairmont, CA 94000
      </address>
    </div>

    <div class="license-note">CA Insurance License #0K72816</div>
  </article>
</body>
</html>
```